BrovaLT BIZ Card, email signature & Stationary

Professional business cards, email signatures and ms word letterhead

Target Market(s)

business owners

Industry/Entity Type

cloud hosting

Contact Information for Business Card

name title office phone number , direct line, fax email address web site

Font styles to use
Other font styles liked:
• something that compliments font in logo

```html
<!DOCTYPE html>
<html lang="en">
<head>
<meta charset="utf-8">
<title>BrovaLT Business Card</title>
<link href="https://fonts.googleapis.com/css2?family=Montserrat:wght@400;500;700&display=swap" rel="stylesheet">
<style>
  :root {
    --page-bg: #3a3b3d;
    --card-white: #ffffff;
    --card-dark: #1d1d1f;
    --brand-red: #e30613;
    --ink: #111111;
    --ink-soft: #222222;
  }
  html, body {
    margin: 0;
    padding: 0;
    width: 1200px;
    height: 1200px;
    overflow: hidden;
    background: var(--page-bg);
    font-family: "Montserrat", sans-serif;
  }
  .canvas {
    position: relative;
    width: 1200px;
    height: 1200px;
  }
  .card {
    position: absolute;
    left: 150px;
    width: 900px;
    height: 514px;
    border-radius: 30px;
    overflow: hidden;
    box-shadow: 0 18px 40px rgba(0,0,0,0.45);
  }
  .card-front {
    top: 60px;
    background: var(--card-white);
  }
  .card-back {
    top: 626px;
    background: var(--card-dark);
    border: 3px solid var(--brand-red);
    box-sizing: border-box;
    display: flex;
    align-items: center;
    justify-content: center;
  }
  .front-bands {
    position: absolute;
    left: 0;
    bottom: 0;
    width: 900px;
    height: 514px;
  }
  .brand-name {
    font-family: "Montserrat", sans-serif;
    font-weight: 500;
    letter-spacing: -1px;
    margin: 0;
  }
  .front-brand {
    position: absolute;
    right: 90px;
    top: 120px;
    font-size: 84px;
    color: var(--ink);
  }
  .back-brand {
    font-size: 76px;
    color: var(--card-white);
  }
  .identity {
    position: absolute;
    left: 70px;
    top: 230px;
  }
  .person-name {
    margin: 0;
    font-weight: 700;
    font-size: 40px;
    color: var(--brand-red);
    line-height: 1;
  }
  .person-title {
    margin: 6px 0 0;
    font-weight: 500;
    font-size: 28px;
    color: var(--ink);
    line-height: 1;
  }
  .contact-list {
    list-style: none;
    margin: 26px 0 0;
    padding: 0 0 0 46px;
  }
  .contact-item {
    display: flex;
    align-items: center;
    gap: 16px;
    font-size: 24px;
    font-weight: 400;
    color: var(--ink-soft);
    height: 36px;
  }
  .contact-icon {
    width: 26px;
    height: 26px;
    flex: none;
    fill: var(--brand-red);
  }
</style>
</head>
<body>
<main class="canvas">

  <section class="card card-front" aria-label="Business card front">
    <svg class="front-bands" viewBox="0 0 900 514" aria-hidden="true">
      <polygon points="0,492 612,462 600,514 0,514" fill="var(--brand-red)"/>
      <polygon points="626,458 900,444 900,514 614,514" fill="var(--ink)"/>
    </svg>

    <p class="brand-name front-brand">BrovaLT</p>

    <div class="identity">
      <h1 class="person-name">FULL NAME</h1>
      <p class="person-title">TITLE</p>
      <ul class="contact-list">
        <li class="contact-item">
          <svg class="contact-icon" viewBox="0 0 24 24"><path d="M6.6 10.8c1.4 2.8 3.8 5.1 6.6 6.6l2.2-2.2c.3-.3.7-.4 1-.2 1.1.4 2.3.6 3.6.6.6 0 1 .4 1 1V20c0 .6-.4 1-1 1C10.6 21 3 13.4 3 4c0-.6.4-1 1-1h3.5c.6 0 1 .4 1 1 0 1.3.2 2.5.6 3.6.1.3 0 .7-.2 1L6.6 10.8z"/></svg>
          <span>(000) 000 0000</span>
        </li>
        <li class="contact-item">
          <svg class="contact-icon" viewBox="0 0 24 24"><path d="M4 7h3V3h10v4h3c1.1 0 2 .9 2 2v10c0 1.1-.9 2-2 2H4c-1.1 0-2-.9-2-2V9c0-1.1.9-2 2-2zm5-2v2h6V5H9zM5 10v2h3v-2H5zm0 4v2h3v-2H5zm5-4v2h3v-2h-3zm0 4v2h3v-2h-3zm5-4v6h4v-6h-4z"/></svg>
          <span>(000) 000 0000</span>
        </li>
        <li class="contact-item">
          <svg class="contact-icon" viewBox="0 0 24 24"><path d="M2 5h20v14H2V5zm2 2v.4l8 5.3 8-5.3V7H4zm0 2.8V17h16V9.8l-8 5.3-8-5.3z"/></svg>
          <span>email@company.com</span>
        </li>
        <li class="contact-item">
          <svg class="contact-icon" viewBox="0 0 24 24"><path d="M12 2a10 10 0 1 0 0 20 10 10 0 0 0 0-20zm6.9 6h-2.9c-.3-1.3-.8-2.5-1.4-3.6 1.8.6 3.4 1.9 4.3 3.6zM12 4c.8 1.2 1.5 2.5 1.9 4h-3.8c.4-1.5 1.1-2.8 1.9-4zM4.3 14a8 8 0 0 1 0-4h3.4c-.1.7-.1 1.3-.1 2s0 1.3.1 2H4.3zm.8 2h2.9c.3 1.3.8 2.5 1.4 3.6-1.8-.6-3.4-1.9-4.3-3.6zM8 8H5.1c.9-1.7 2.5-3 4.3-3.6C8.8 5.5 8.3 6.7 8 8zm4 12c-.8-1.2-1.5-2.5-1.9-4h3.8c-.4 1.5-1.1 2.8-1.9 4zm2.3-6H9.7c-.1-.7-.2-1.3-.2-2s.1-1.3.2-2h4.6c.1.7.2 1.3.2 2s-.1 1.3-.2 2zm.3 5.6c.6-1.1 1.1-2.3 1.4-3.6h2.9c-.9 1.7-2.5 3-4.3 3.6zm1.7-5.6c.1-.7.1-1.3.1-2s0-1.3-.1-2h3.4a8 8 0 0 1 0 4h-3.4z"/></svg>
          <span>www.company.com</span>
        </li>
      </ul>
    </div>
  </section>

  <section class="card card-back" aria-label="Business card back">
    <p class="brand-name back-brand">BrovaLT</p>
  </section>

</main>
</body>
</html>
```